Stonewell Holdings

Professional looking business card using darker colours
I do not yet have a logo for the company so feel free to suggest
The business is based on consultancy and project management
Based in Melbourne
Business card can omit the word "Holdings" and can be Stonewell consulting etc.

Contact Name on card : Ravi Pelunkoda Contact number : +61433 512 604 Email address will be confirmed shortly.

```html
<!DOCTYPE html>
<html lang="en">
<head>
<meta charset="utf-8">
<title>Stonewell Consulting – Business Card</title>
<link href="https://fonts.googleapis.com/css2?family=Didact+Gothic&display=swap" rel="stylesheet">
<style>
  :root {
    --backdrop: #9a9a9a;
    --card-black: #0d0d0d;
    --card-white: #efefef;
    --charcoal: #4a4a4a;
    --ink: #2b2b2b;
    --wine: #7a1524;
    --wine-deep: #5a0f1a;
    --paper-light: #f4f4f4;
  }
  * { margin: 0; padding: 0; box-sizing: border-box; }
  html, body { width: 1200px; height: 1048px; overflow: hidden; }
  body {
    background: radial-gradient(ellipse at 50% 45%, #c4c4c4 0%, var(--backdrop) 100%);
    font-family: "Didact Gothic", "Century Gothic", sans-serif;
    position: relative;
  }
  .card {
    position: absolute;
    left: 220px;
    width: 760px;
    height: 434px;
    border-radius: 4px;
    box-shadow: 0 10px 30px rgba(0,0,0,.35);
    overflow: hidden;
  }
  .card--back { top: 60px; background: var(--card-black); }
  .card--front {
    top: 554px;
    background: linear-gradient(160deg, #ffffff 0%, var(--card-white) 60%, #dcdcdc 100%);
  }

  .wordmark {
    position: absolute;
    display: flex;
    align-items: center;
    gap: 14px;
    letter-spacing: .32em;
    font-size: 24px;
    line-height: 1;
    text-transform: uppercase;
  }
  .wordmark__square { width: 22px; height: 22px; background: var(--wine); flex: none; }
  .card--back .wordmark { left: 50%; top: 50%; transform: translate(-50%, -50%); color: var(--paper-light); }
  .card--front .wordmark { left: 56px; top: 118px; color: var(--charcoal); font-size: 20px; }

  .contact { position: absolute; left: 420px; top: 150px; color: var(--ink); }
  .contact__name { font-size: 27px; letter-spacing: .03em; }
  .contact__title { font-size: 19px; color: var(--wine); margin-top: 2px; }
  .contact__row { display: flex; align-items: center; gap: 18px; font-size: 21px; margin-top: 14px; letter-spacing: .03em; }
  .contact__row:first-of-type { margin-top: 10px; }
  .contact__icon { width: 22px; height: 18px; flex: none; }

  .bands { position: absolute; left: 0; bottom: 0; width: 760px; height: 88px; }
</style>
</head>
<body>

  <section class="card card--back" aria-label="Card reverse">
    <div class="wordmark"><span class="wordmark__square"></span>Stonewell Consulting</div>
  </section>

  <section class="card card--front" aria-label="Card front">
    <div class="wordmark"><span class="wordmark__square"></span>Stonewell Consulting</div>

    <div class="contact">
      <div class="contact__name">Ravi Pelunkoda</div>
      <div class="contact__title">Job Title</div>
      <div class="contact__row">
        <svg class="contact__icon" viewBox="0 0 22 18" aria-hidden="true">
          <path d="M1 6 Q11 -1 21 6 L18 8 L15 6 L15 4 Q11 2.5 7 4 L7 6 L4 8 Z" fill="#7a1524"/>
          <rect x="4" y="9" width="14" height="8" rx="1.5" fill="#7a1524"/>
          <circle cx="11" cy="13" r="2.2" fill="#f4f4f4"/>
        </svg>
        <span>+61433 512 604</span>
      </div>
      <div class="contact__row">
        <svg class="contact__icon" viewBox="0 0 22 18" aria-hidden="true">
          <rect x="1" y="2" width="20" height="14" fill="#7a1524"/>
          <path d="M1 2 L11 10 L21 2" fill="none" stroke="#f4f4f4" stroke-width="1.4"/>
        </svg>
        <span>ravi@stonewellco.com.au</span>
      </div>
    </div>

    <svg class="bands" viewBox="0 0 760 88" preserveAspectRatio="none" aria-hidden="true">
      <polygon points="0,0 298,0 270,88 0,88" fill="#4a4a4a"/>
      <polygon points="304,0 760,0 760,88 276,88" fill="#7a1524"/>
    </svg>
  </section>

</body>
</html>
```